buseisness card

design a card that similar to my web site
BRIXENTAPLORLLC .COM

Contact Information for Business Card

NAME PHONE # WEBSITE EMAIL AND DISCTIPTION OF WHAT WE DO

Colors
0054AA
0677BA
7BADD7
CADEEF
E8F1F8

Requirements
Must have
• lOGO AND DETAILS
Nice to have
• I LIKE THE WATER LIKE ON MY WEB SITE

```html
<!DOCTYPE html>
<html lang="en">
<head>
<meta charset="utf-8">
<title>Brixentaplor Business Card</title>
<link rel="stylesheet" href="https://fonts.googleapis.com/css2?family=Montserrat:wght@700&family=Arimo:wght@400;700&display=swap">
<style>
  :root {
    --backdrop: #1e1e1e;
    --deep-navy: #0b1c26;
    --sea-teal: #1d5a6e;
    --sea-mid: #15404f;
    --brand-blue: #2080b8;
    --accent-blue: #33aee0;
    --paper: #ffffff;
    --text-light: #ffffff;
  }
  * { margin: 0; padding: 0; box-sizing: border-box; }
  html, body {
    width: 1200px; height: 988px; overflow: hidden;
    background: var(--backdrop);
  }
  .stage { position: relative; width: 1200px; height: 988px; }
  .card {
    position: absolute; width: 560px; height: 320px;
    border-radius: 22px; overflow: hidden;
  }
  /* back side */
  .card-back { left: 70px; top: 140px; }
  .water-fill {
    position: absolute; inset: 0;
    background: linear-gradient(180deg, var(--sea-teal) 0%, var(--sea-mid) 45%, var(--deep-navy) 100%);
  }
  .back-brand {
    position: absolute; left: 0; right: 0; top: 130px;
    display: flex; align-items: center; justify-content: center; gap: 14px;
  }
  .brand-dot {
    width: 40px; height: 40px; border-radius: 50%;
    border: 4px solid var(--text-light);
  }
  .back-brand .brand-name {
    font-family: "Montserrat", sans-serif; font-weight: 700;
    font-size: 34px; letter-spacing: 1px; color: var(--text-light);
  }
  /* front side */
  .card-front { left: 570px; top: 520px; background: var(--paper); }
  .front-wave { position: absolute; inset: 0; }
  .front-brand {
    position: absolute; left: 140px; top: 36px;
    font-family: "Montserrat", sans-serif; font-weight: 700;
    font-size: 34px; letter-spacing: 1px; color: var(--brand-blue);
  }
  .contact {
    position: absolute; left: 112px; top: 186px;
    font-family: "Arimo", sans-serif; color: var(--text-light);
  }
  .contact .person-name { font-weight: 700; font-size: 18px; letter-spacing: .5px; line-height: 1.15; }
  .contact .person-role { font-size: 11px; line-height: 1.2; margin: 0 0 6px 8px; }
  .contact .address { font-size: 11.5px; line-height: 1.3; margin-left: 22px; margin-bottom: 6px; }
  .contact-line {
    display: flex; align-items: center; gap: 6px;
    font-size: 11.5px; line-height: 1.4; margin-left: 22px;
  }
  .contact-line svg { width: 11px; height: 11px; flex: none; }
</style>
</head>
<body>
<main class="stage">

  <section class="card card-back">
    <div class="water-fill" role="img" aria-label="Underwater photograph of the sea surface seen from below, in deep teal and navy tones"></div>
    <div class="back-brand">
      <span class="brand-dot"></span>
      <span class="brand-name">BRIXENTAPLOR</span>
    </div>
  </section>

  <section class="card card-front">
    <svg class="front-wave" viewBox="0 0 560 320" preserveAspectRatio="none" aria-hidden="true">
      <path d="M552 66 C540 122 515 148 470 154 C360 162 250 150 168 158" fill="none" stroke="var(--accent-blue)" stroke-width="6"/>
      <path d="M560 90 C 548 135 520 160 470 165 C 360 172 250 160 170 168 C 100 176 55 225 30 320 L560 320 Z" fill="var(--brand-blue)"/>
      <circle cx="465" cy="150" r="58" fill="var(--paper)"/>
      <circle cx="465" cy="150" r="50" fill="var(--brand-blue)"/>
    </svg>
    <div class="front-brand">BRIXENTAPLOR</div>
    <div class="contact">
      <div class="person-name">MARLON TEAGUE</div>
      <div class="person-role">Owner</div>
      <div class="address">1180 Alder Creek Road.<br>Dunmore, AB 50322</div>
      <div class="contact-line">
        <svg viewBox="0 0 12 12"><path d="M2 1h3l1 3-1.5 1a6 6 0 0 0 2.5 2.5L8 6l3 1v3a1 1 0 0 1-1 1A9 9 0 0 1 1 2a1 1 0 0 1 1-1z" fill="var(--text-light)"/></svg>
        <span>(123) 555-0147</span>
      </div>
      <div class="contact-line">
        <svg viewBox="0 0 12 12"><rect x="1" y="2.5" width="10" height="7" fill="var(--text-light)"/><path d="M1 2.5l5 4 5-4" fill="none" stroke="var(--brand-blue)" stroke-width="1"/></svg>
        <span>info@brixentaplorllc .com</span>
      </div>
      <div class="contact-line">
        <svg viewBox="0 0 12 12"><circle cx="6" cy="6" r="5" fill="var(--text-light)"/><path d="M1 6h10M6 1c-2 3-2 7 0 10M6 1c2 3 2 7 0 10" fill="none" stroke="var(--brand-blue)" stroke-width=".8"/></svg>
        <span>www.brixentaplorllc .com</span>
      </div>
    </div>
  </section>

</main>
</body>
</html>
```